Pull up banners. Tradeshow-to draw people to our booth

Medical Spa in a Bridal Show. Skin and body solutions for all skin types. We need to draw as much attention to get people to come to our booth #76.

We did up a rough draft in one of the attachments. The other is to show you our back drop at the booth, that way you can get a feel of colours, logos, services, etc.

I have also attached our #1 service for brides and grooms. Please use those words.

Fear no mirror for your wedding day.

Eat, drink, shrink for your wedding day.

I need 2 banner designed in total. For the entrance area.

31.3”w x 89.75”h with high –res PDF files
Updates

Target Market(s)

Brides

Industry/Entity Type

Medical

Requirements
Must have
• A pictures of a bride and groom

```html
<!DOCTYPE html>
<html lang="en">
<head>
<meta charset="utf-8">
<title>Aurelle Medispa – Bridal Show Banner</title>
<link href="https://fonts.googleapis.com/css2?family=Lato:wght@400;700;900&family=Playfair+Display:ital,wght@0,700;0,900;1,700&display=swap" rel="stylesheet">
<style>
  :root {
    --page: #ecebe8;
    --white: #ffffff;
    --purple: #6a3d9a;
    --purple-deep: #4e2a78;
    --magenta: #d6338a;
    --pink-soft: #f7dcea;
    --pink-band: #f3c6dd;
    --blue: #2f86c9;
    --blue-deep: #1f6aa8;
    --ink: #3a2a4a;
  }
  * { margin: 0; padding: 0; box-sizing: border-box; }
  html, body { width: 800px; height: 1200px; overflow: hidden; }
  body {
    background: var(--page);
    font-family: "Lato", sans-serif;
    display: flex; align-items: center; justify-content: center;
  }
  .banner {
    width: 410px; height: 1176px;
    background: var(--white);
    display: flex; flex-direction: column;
    box-shadow: 0 2px 8px rgba(0,0,0,.15);
  }
  .accent-rule { height: 8px; background: var(--magenta); }
  .header {
    height: 74px; display: flex; align-items: center; justify-content: space-between;
    padding-left: 18px;
  }
  .brand { display: flex; align-items: center; gap: 8px; color: var(--purple); font-weight: 900; font-size: 21px; }
  .brand-dot { width: 16px; height: 16px; border-radius: 50%; background: var(--purple); }
  .booth-tab {
    background: var(--purple); color: var(--white); font-weight: 900; font-size: 20px;
    padding: 12px 18px 12px 24px; border-radius: 22px 0 0 22px;
  }
  .hero {
    position: relative; height: 470px;
    background: linear-gradient(180deg, #d9d6d2 0%, #bfb6b0 35%, #efe8e6 70%, #f6e4ec 100%);
  }
  .hero-title {
    position: absolute; left: 0; right: 0; bottom: 18px; text-align: center;
    font-family: "Playfair Display", serif; font-weight: 900; font-size: 50px;
    color: var(--magenta); letter-spacing: 1px;
  }
  .tagline-band {
    height: 52px; background: var(--purple); color: var(--white);
    display: flex; align-items: center; justify-content: center;
    font-family: "Playfair Display", serif; font-style: italic; font-weight: 700; font-size: 19px;
  }
  .promo-strip {
    height: 46px; display: flex; align-items: center; justify-content: space-between;
    padding: 0 14px; border-bottom: 3px solid var(--blue);
  }
  .promo-strip .brand { font-size: 15px; }
  .promo-strip .brand-dot { width: 11px; height: 11px; }
  .promo-line { color: var(--blue-deep); font-weight: 900; font-size: 15px; }
  .service-grid {
    height: 250px; padding: 6px; display: grid; gap: 5px;
    grid-template-columns: 1fr 1fr 1fr; grid-template-rows: 70px 82px 82px;
  }
  .service { background: var(--blue); color: var(--white); padding: 8px 10px; }
  .service h3 { font-size: 14px; font-weight: 900; margin-bottom: 4px; }
  .service p { font-size: 11px; line-height: 1.3; }
  .span-half { grid-column: span 1; }
  .wide { grid-column: span 2; }
  .row-first-a { grid-column: 1 / span 2; }
  .row-first-b { grid-column: 3 / span 1; }
  .photo { background: linear-gradient(135deg, #cfc3bd, #8d7f7a 60%, #e9dfe0); }
  .footer {
    flex: 1; position: relative; background: linear-gradient(180deg, var(--pink-soft), var(--pink-band));
    display: flex; flex-direction: column; align-items: center; justify-content: center; gap: 8px;
    color: var(--ink); text-align: center; padding: 0 30px;
  }
  .footer-lead { font-family: "Playfair Display", serif; font-weight: 700; font-size: 17px; color: var(--purple-deep); }
  .footer-note { font-size: 13px; }
  .floral {
    position: absolute; left: 14px; bottom: 16px; width: 90px; height: 46px;
    background: radial-gradient(circle, #b04a93 0%, #d98cbc 60%, rgba(217,140,188,0) 75%);
  }
</style>
</head>
<body>
  <main class="banner">
    <div class="accent-rule"></div>
    <header class="header">
      <div class="brand"><span class="brand-dot"></span>Aurelle Medispa</div>
      <div class="booth-tab">Booth #76</div>
    </header>

    <section class="hero" role="img" aria-label="Photo of a bride and groom embracing, the bride holding a pink and white bouquet">
      <h1 class="hero-title">Eat Drink Shrink</h1>
    </section>

    <div class="tagline-band">Fear no Mirror for your Wedding Day</div>

    <div class="promo-strip">
      <div class="brand"><span class="brand-dot"></span>Aurelle Medispa</div>
      <div class="promo-line">Say Yes to your glow</div>
    </div>

    <section class="service-grid">
      <div class="service row-first-a"><h3>Body Contouring</h3><p>Shape and tone before the big day.</p></div>
      <div class="service row-first-b"><h3>Skin Renewal</h3><p>Clear, bright skin for every photo.</p></div>
      <div class="photo" role="img" aria-label="Photo of a bride and groom"></div>
      <div class="service wide"><h3>Bridal Packages</h3><p>Plans for brides, grooms and the whole party.</p></div>
      <div class="photo" role="img" aria-label="Photo of a smiling bride"></div>
      <div class="service"><h3>Visit Booth #76</h3><p>Free consults today.</p></div>
      <div class="photo" role="img" aria-label="Photo of a wedding couple"></div>
    </section>

    <footer class="footer">
      <p class="footer-lead">Skin and body solutions for all skin types</p>
      <p class="footer-note">Book your bridal consult at the show</p>
      <div class="floral" role="img" aria-label="Decorative purple floral spray"></div>
    </footer>
  </main>
</body>
</html>
```